Komira online ordering platform looking for a great web design

Komira - from the Vietnamese words Lộc Vân meaning financial success.
Background
Komira is an online ordering platform for small retail businesses (corner stores). The idea is that small retailers will use the website to order their supplies. From this we will utilise the group buying to get better deals for them that they could not achieve individually.
We are looking for a simple but stylish design for our ordering page. The layout needs to be efficient, logical and self explanatory.
Products to be sold on the site are FMCG (fast moving consumer goods). Potential to be 000's of items.
Considerations
- end users are not technologically adept.
- Users are generally older so small print will not be well received.
- Use of touch screen monitors to select/change items so spacing in design is vital.
- Logical display of category and sub-categories.
- Easy selection of products to order as well as modification of quantity.
- Shopping cart with easy change of item quantity.
- List of items for ordering can be paginated.
- Items listed will have image for easy identification.
- Search box
- Format should be in psd (photoshop) or complete html/css
- All this information needs to be displayed on the one page.
Product information to contain the following:
- Image
- Price
- Product name
- Size
Area for prominent display of specials without crowding the product information.

```html
<!DOCTYPE html>
<html lang="en">
<head>
<meta charset="utf-8">
<title>Komira – Intelligent Retail Ordering</title>
<link href="https://fonts.googleapis.com/css2?family=Open+Sans:wght@400;600;700&family=Roboto+Condensed:wght@700&display=swap" rel="stylesheet">
<style>
:root{
  --teal:#1b6e86;
  --teal-dark:#14566b;
  --btn:#2f86a6;
  --btn-dark:#1f6784;
  --orange:#ee7d1a;
  --ink:#222;
  --muted:#555;
  --line:#d9d9d9;
  --hero-1:#bff0ff;
  --hero-2:#33c3ee;
  --hero-3:#1c9fd6;
  --footer-1:#1d6a86;
  --footer-2:#0f3f55;
  --field:#e6e6e6;
}
*{box-sizing:border-box;margin:0;padding:0}
html,body{width:964px;height:1200px;overflow:hidden}
body{position:relative;background:#fff;font-family:"Open Sans",Arial,sans-serif;color:var(--ink)}
.abs{position:absolute}

/* header */
.site-header{position:absolute;left:0;top:0;width:964px;height:75px;background:#f3f3f1}
.brand{position:absolute;left:156px;top:10px;font-family:"Open Sans",Arial,sans-serif;font-weight:700;font-size:42px;color:var(--teal);letter-spacing:1px}
.member{position:absolute;left:642px;top:20px;font-size:11px;font-weight:600;color:#333}
.member a{color:var(--teal);text-decoration:none}
.member .sep{margin:0 6px;color:#555}
.login{position:absolute;left:770px;top:17px;width:66px;height:21px;background:linear-gradient(#2a7fa0,#1c6785);color:#fff;font-size:11px;font-weight:600;line-height:21px;padding-left:13px;border-radius:2px}
.login i{position:absolute;right:6px;top:5px;width:11px;height:11px;border-radius:50%;background:#0f4b63;font-style:normal;font-size:7px;line-height:11px;text-align:center}

/* nav */
.main-nav{position:absolute;left:0;top:75px;width:964px;height:34px;background:#f6f6f6;border-top:1px solid #ddd;border-bottom:1px solid #ddd}
.main-nav span{position:absolute;top:8px;font-size:13px;transform:translateX(-50%);color:#222}
.main-nav .div{position:absolute;top:0;width:1px;height:33px;background:#dcdcdc}

/* hero */
.hero{position:absolute;left:0;top:109px;width:964px;height:361px;background:radial-gradient(ellipse 420px 300px at 470px 180px,var(--hero-1),var(--hero-2) 70%,var(--hero-3))}
.hero h1{position:absolute;left:158px;top:27px;font-size:18px;line-height:26px;font-weight:700;color:var(--teal-dark)}
.hero h1 em{font-style:normal;color:var(--orange)}
.more{position:absolute;left:159px;top:87px;width:65px;height:21px;background:linear-gradient(#2b7ea0,#175f7c);color:#fff;font-size:11px;font-weight:700;line-height:21px;padding-left:13px;border:1px solid #0e4c65}
.more i{position:absolute;right:6px;top:5px;width:10px;height:10px;border-radius:50%;background:#0f4b63;font-style:normal;font-size:7px;line-height:10px;text-align:center}
.hero-art{position:absolute;left:186px;top:140px;width:291px;height:175px;border-radius:6px;background:linear-gradient(135deg,#9aa2a8,#3b78c8 45%,#c9b98e)}
.hero-photo{position:absolute;left:559px;top:16px;width:405px;height:345px;background:linear-gradient(160deg,#e8c3a4 0%,#c9a184 22%,#223553 40%,#17243a 100%);border-radius:160px 0 0 0}
.slider-bar{position:absolute;left:0;bottom:0;width:964px;height:32px;background:rgba(20,90,130,.35)}
.slider-bar svg{position:absolute;left:446px;top:7px}

/* intro */
.intro-title{position:absolute;left:0;width:964px;top:503px;text-align:center;font-family:"Roboto Condensed",Arial,sans-serif;font-size:18px;color:var(--teal-dark)}
.intro-sub{position:absolute;left:0;width:964px;top:533px;text-align:center;font-family:"Roboto Condensed",Arial,sans-serif;font-size:13px;color:#222}
.intro-sub b{color:var(--btn)}

/* panel */
.panel{position:absolute;left:130px;top:560px;width:699px;height:512px;background:#fff;box-shadow:0 0 10px rgba(0,0,0,.12)}
.search-title{position:absolute;left:147px;top:572px;font-size:12px;font-weight:700;color:var(--teal)}
.search-rule{position:absolute;left:141px;top:596px;width:167px;border-top:1px dashed #ccc}
.cart{position:absolute;right:149px;top:574px;font-size:12px;color:#333;display:flex;align-items:center;gap:5px}
.cart b{font-weight:400;color:var(--teal)}

.filter-label{position:absolute;left:148px;font-size:9.5px;color:#333}
.select{position:absolute;left:148px;width:152px;height:20px;background:var(--field);border:1px solid #ddd;font-size:9.5px;line-height:18px;padding-left:5px;color:#333}
.select::after{content:"";position:absolute;right:0;top:-1px;width:20px;height:20px;background:#3e8fae}
.select svg{position:absolute;right:6px;top:6px;z-index:1}
.range-tag{position:absolute;top:849px;font-size:9px;color:var(--btn)}
.field{position:absolute;top:858px;height:20px;background:var(--field);border:1px solid #ddd;font-size:9.5px;line-height:18px;padding-left:5px}
.submit{position:absolute;left:234px;top:891px;width:66px;height:20px;background:linear-gradient(#2b7ea0,#175f7c);color:#fff;font-size:11px;font-weight:700;text-align:center;line-height:20px}

.promo{position:absolute;left:145px;top:928px;width:156px;height:121px;border-radius:5px;background:linear-gradient(#f6c93c,#e6a014);border:2px solid #d98a10}
.promo .gift{position:absolute;left:14px;top:14px;width:42px;height:46px;border-radius:4px;background:linear-gradient(#e65b2a,#c0321a)}
.promo h3{position:absolute;left:60px;top:12px;width:90px;text-align:center;font-size:16px;line-height:19px;font-weight:400;color:#b3261a}
.promo h3 span{color:#fff}
.promo .strip{position:absolute;left:5px;right:5px;top:88px;height:26px;background:#a8291a;border-radius:2px}
.promo .strip p{position:absolute;left:6px;top:5px;font-size:6px;line-height:8px;color:#fff;width:70px}
.promo .strip a{position:absolute;right:6px;top:4px;width:50px;height:17px;background:linear-gradient(#f6b030,#e0801a);border:1px solid #ffd37a;font-size:7px;color:#fff;text-align:center;line-height:15px;text-decoration:none}

.col-rule{position:absolute;left:314px;top:597px;height:452px;border-left:1px dashed #ccc}

/* product table */
.table-head{position:absolute;left:314px;top:597px;width:503px;height:35px;background:linear-gradient(#3b8fb0,#2a7999);color:#fff;font-size:11px;font-weight:600}
.table-head span{position:absolute;top:10px}
.table-head .c{transform:translateX(-50%)}
.table-head .sep{position:absolute;top:0;width:1px;height:35px;background:#5ea6c2}
.row{position:absolute;left:322px;width:495px;height:86px}
.thumb{position:absolute;left:0;top:0;width:94px;height:84px;border:1px solid #ddd;background:linear-gradient(#fff,#eef2f6);padding:4px}
.thumb div{width:100%;height:100%;background:linear-gradient(90deg,#fff 25%,#7f98b8 40%,#233 55%,#1a1a1a 70%,#fff 78%)}
.row h4{position:absolute;left:109px;top:6px;font-size:9.5px;font-weight:400;color:var(--teal)}
.row p{position:absolute;left:109px;top:19px;width:165px;font-size:9.5px;line-height:13px;color:#333}
.price{position:absolute;left:304px;top:26px;font-size:9.5px;color:#333}
.unit{position:absolute;left:360px;top:19px;width:31px;height:14px;border:1px solid #ccc;font-size:9px;text-align:center;line-height:12px}
.add{position:absolute;left:414px;top:12px;width:70px;height:28px;background:linear-gradient(#3590b2,#226f8e);border:1px solid #1b6380;border-radius:2px;color:#fff;font-size:9.5px;text-align:center;line-height:26px}

.pager{position:absolute;top:1037px;height:20px;font-size:8px;color:#fff;text-align:center;line-height:20px;border-radius:2px;background:linear-gradient(#555,#2b2b2b)}
.pager.o{background:linear-gradient(#f7a64a,#e47a12)}
.pager.on{background:#111}

/* footer */
.site-footer{position:absolute;left:0;top:1078px;width:964px;height:122px;background:linear-gradient(var(--footer-1),var(--footer-2));border-top:3px solid #2d88aa}
.foot-links{position:absolute;top:23px;left:0;width:964px;text-align:center;font-size:12px;color:#fff}
.foot-links a{color:#fff;text-decoration:none}
.foot-links a.current{color:#4cc3f0;text-decoration:underline}
.foot-links .s{margin:0 12px}
.copyright{position:absolute;top:47px;left:0;width:964px;text-align:center;font-size:12px;color:#e8f3f7}
.social{position:absolute;top:74px;width:25px;height:26px;background:#0c3346;border:1px solid #1d5a73}
</style>
</head>
<body>

<header class="site-header">
  <div class="brand">Komira</div>
  <div class="member">Member <a href="#">Registration</a><span class="sep">|</span></div>
  <div class="login">Login<i>v</i></div>
</header>

<nav class="main-nav">
  <svg class="abs" style="left:168px;top:10px" width="14" height="13" viewBox="0 0 14 13"><path d="M7 1 L13 6.5 H11 V12 H8.5 V8.5 H5.5 V12 H3 V6.5 H1 Z" fill="#2a7fa0"/></svg>
  <span style="left:264px">About Us</span>
  <div class="div" style="left:325px"></div>
  <span style="left:417px">Delivery Information</span>
  <div class="div" style="left:509px"></div>
  <span style="left:591px">How does it work</span>
  <div class="div" style="left:679px"></div>
  <span style="left:727px">Faq</span>
  <div class="div" style="left:770px"></div>
  <span style="left:810px">Contact</span>
</nav>

<section class="hero">
  <h1>Welcome to <em>Intelligent Retail</em><br>Your <em>one stop</em> ordering site</h1>
  <div class="more">More<i>&gt;</i></div>
  <div class="hero-art" role="img" aria-label="Illustration of delivery workers carrying parcels out of a computer screen"></div>
  <div class="hero-photo" role="img" aria-label="Photo of a smiling businessman in a suit gesturing toward the welcome message"></div>
  <div class="slider-bar">
    <svg width="72" height="18" viewBox="0 0 72 18">
      <path d="M10 2 L3 9 L10 16" stroke="#fff" stroke-width="1.8" fill="none"/>
      <circle cx="23" cy="9" r="3.2" fill="#cfeefb"/><circle cx="34" cy="9" r="3.2" fill="#1c6e8c"/><circle cx="45" cy="9" r="3.2" fill="#1c6e8c"/>
      <path d="M58 2 L65 9 L58 16" stroke="#fff" stroke-width="1.8" fill="none"/>
    </svg>
  </div>
</section>

<h2 class="intro-title">Welcome to our online Retailling Solution</h2>
<p class="intro-sub">Guaranteed the best ordering experience, <b>bla, bla, bla</b></p>

<main class="panel"></main>

<div class="search-title">Search your products below :</div>
<div class="search-rule"></div>
<div class="cart">
  <svg width="13" height="12" viewBox="0 0 13 12"><path d="M1 1 H3 L4.5 8 H11 L12 3 H3.6" stroke="#333" stroke-width="1.2" fill="none"/><circle cx="5" cy="10.5" r="1" fill="#333"/><circle cx="10" cy="10.5" r="1" fill="#333"/></svg>
  <span><b>2 items</b> in your cart</span>
</div>

<aside>
  <div class="filter-label" style="top:610px">Choose Category :</div>
  <div class="select" style="top:626px">Clothes<svg width="8" height="7" viewBox="0 0 8 7"><path d="M0 0 H8 L4 7Z" fill="#fff"/></svg></div>
  <div class="filter-label" style="top:655px">Item Name :</div>
  <div class="select" style="top:670px">TShirt<svg width="8" height="7" viewBox="0 0 8 7"><path d="M0 0 H8 L4 7Z" fill="#fff"/></svg></div>
  <div class="filter-label" style="top:700px">Brand</div>
  <div class="select" style="top:715px">Corvo<svg width="8" height="7" viewBox="0 0 8 7"><path d="M0 0 H8 L4 7Z" fill="#fff"/></svg></div>
  <div class="filter-label" style="top:744px">Sex :</div>
  <div class="select" style="top:759px">Men<svg width="8" height="7" viewBox="0 0 8 7"><path d="M0 0 H8 L4 7Z" fill="#fff"/></svg></div>
  <div class="filter-label" style="top:787px">Size :</div>
  <div class="select" style="top:803px">XXL<svg width="8" height="7" viewBox="0 0 8 7"><path d="M0 0 H8 L4 7Z" fill="#fff"/></svg></div>
  <div class="filter-label" style="top:833px">Price Range :</div>
  <div class="range-tag" style="left:148px">From</div>
  <div class="range-tag" style="left:225px">To</div>
  <div class="field" style="left:148px;width:70px">$ 120</div>
  <div class="field" style="left:225px;width:75px">$ 500</div>
  <div class="submit">Submit</div>

  <div class="promo">
    <div class="gift" role="img" aria-label="Illustration of a wrapped gift box with a red bow"></div>
    <h3>Latest<br>Brand<br><span>ADDED</span></h3>
    <div class="strip">
      <p>Weekly deals on new stock.</p>
      <a href="#">Read More</a>
    </div>
  </div>
</aside>

<div class="col-rule"></div>

<div class="table-head">
  <span style="left:9px">Your Product</span>
  <div class="sep" style="left:108px"></div>
  <span style="left:117px">Item Description</span>
  <div class="sep" style="left:285px"></div>
  <span class="c" style="left:323px">Price</span>
  <div class="sep" style="left:356px"></div>
  <span class="c" style="left:384px">Unit</span>
  <div class="sep" style="left:411px"></div>
  <span class="c" style="left:457px">Action</span>
</div>

<div class="row" style="top:641px">
  <div class="thumb"><div role="img" aria-label="Photo of a man in a formal shirt and tie holding a jacket"></div></div>
  <h4>Corvo Full Shirt Formal</h4>
  <p>Lorem ipsum dolor sit amet, consectetur adipisicing elit, sed do eiusmod tempor incididunt ut labore et dolore magna aliqua.</p>
  <div class="price">$220</div>
  <div class="unit">2</div>
  <div class="add">Add to Cart</div>
</div>
<div class="row" style="top:741px">
  <div class="thumb"><div role="img" aria-label="Photo of a man in a formal shirt and tie holding a jacket"></div></div>
  <h4>Corvo Full Shirt Formal</h4>
  <p>Lorem ipsum dolor sit amet, consectetur adipisicing elit, sed do eiusmod tempor incididunt ut labore et dolore magna aliqua.</p>
  <div class="price">$220</div>
  <div class="unit"></div>
  <div class="add">Add to Cart</div>
</div>
<div class="row" style="top:843px">
  <div class="thumb"><div role="img" aria-label="Photo of a man in a formal shirt and tie holding a jacket"></div></div>
  <h4>Corvo Full Shirt Formal</h4>
  <p>Lorem ipsum dolor sit amet, consectetur adipisicing elit, sed do eiusmod tempor incididunt ut labore et dolore magna aliqua.</p>
  <div class="price">$220</div>
  <div class="unit"></div>
  <div class="add">Add to Cart</div>
</div>
<div class="row" style="top:943px">
  <div class="thumb"><div role="img" aria-label="Photo of a man in a formal shirt and tie holding a jacket"></div></div>
  <h4>Corvo Full Shirt Formal</h4>
  <p>Lorem ipsum dolor sit amet, consectetur adipisicing elit, sed do eiusmod tempor incididunt ut labore et dolore magna aliqua.</p>
  <div class="price">$220</div>
  <div class="unit"></div>
  <div class="add">Add to Cart</div>
</div>

<nav aria-label="Pagination">
  <div class="pager o" style="left:531px;width:43px">« First</div>
  <div class="pager" style="left:577px;width:20px">«</div>
  <div class="pager" style="left:600px;width:20px">1</div>
  <div class="pager on" style="left:624px;width:20px">2</div>
  <div class="pager" style="left:647px;width:20px">3</div>
  <div class="pager" style="left:670px;width:20px">...</div>
  <div class="pager" style="left:693px;width:20px">8</div>
  <div class="pager" style="left:716px;width:20px">9</div>
  <div class="pager o" style="left:739px;width:21px">»</div>
  <div class="pager o" style="left:763px;width:43px">Last »</div>
</nav>

<footer class="site-footer">
  <div class="foot-links">
    <a href="#" class="current">Home</a><span class="s">|</span><a href="#">About Us</a><span class="s">|</span><a href="#">Delivery Information</a><span class="s">|</span><a href="#">How does it work</a><span class="s">|</span><a href="#">Faq</a><span class="s">|</span><a href="#">Contact</a>
  </div>
  <div class="copyright">Copyright@2013, Komira, All rights are reserved.</div>
  <div class="social" style="left:453px"></div>
  <div class="social" style="left:481px"></div>
</footer>

</body>
</html>
```